Heart Rate Game Display Graphic

We need a unique layout / info-graphic for our heart rate software to display an individuals hear rate, HR%, and other data together within a larger class of up to 40 other users. Graphics should be colorful, dynamic, and intuitive.

Target Market(s)

Group Fitness Classes

Font styles to use
Sans Serif

Colors

Designer to choose colors to be used in the design.

Requirements
Must have
• Individual Box must contain data field or graphic representation of:
• User Name
• Heart Rate %
• Points Earned / % Accuracy
Nice to have
• thinking other shape design that easily integrates with 40+ of the same shape. Looking for depth of design and or some 3d visualizations. Competing companies:
• https://www.pulsevane.org/
• https://www.trovo.com/
• https://www.kestra.com/us-en/club
• https://bravulo.com/
• https://dornaly.fit/personal-trainer/
• https://www.quelvanta.io/Solutions/Heart-Rate-Training
• http://wamble.corvinladesystems.com/
• https://pell-tander.com/explore/pell-tander-indoor-cycling-app/
Should not have
• should NOT be just be plain squares representing each client.

```html
<!DOCTYPE html>
<html lang="en">
<head>
<meta charset="utf-8">
<title>Heart Rate Class Display</title>
<link rel="stylesheet" href="https://fonts.googleapis.com/css2?family=Open+Sans:wght@400;500;600&display=swap">
<style>
  :root{
    --page:#80a9dc;
    --screen:#162039;
    --bar:#141c32;
    --cyan:#22e4f2;
    --cyan-line:#1fb8cc;
    --plate-top:#14306a;
    --plate-bottom:#0a1a3e;
    --pill:#0a1530;
    --rail:#1b2436;
    --green:#29e021;
    --orange:#ff9a12;
    --red:#ee1a1a;
    --muted:#7f93b8;
    --white:#ffffff;
  }
  *{box-sizing:border-box;margin:0;padding:0}
  html,body{width:1200px;height:929px;overflow:hidden}
  body{background:var(--page);font-family:"Open Sans",sans-serif;position:relative}
  .screen{position:absolute;left:0;top:127px;width:1200px;height:675px;background:var(--screen);overflow:hidden}

  /* header */
  .topbar{position:absolute;left:0;top:0;width:100%;height:62px;background:var(--bar);display:flex;align-items:center}
  .back-btn{position:absolute;left:22px;top:19px}
  .system-title{position:absolute;left:50%;top:12px;transform:translateX(-50%);border:1.5px solid #9aa4b8;color:var(--white);font-size:18px;font-weight:500;padding:5px 18px;line-height:24px}
  .account{position:absolute;right:80px;top:13px;display:flex;align-items:center;gap:9px;color:var(--white);font-size:15px}
  .settings-btn{position:absolute;right:15px;top:18px}

  /* stage */
  .stage{position:absolute;left:0;top:62px;width:100%;height:551px;background:radial-gradient(ellipse at 50% 45%,#1f3a4f 0%,#19293f 45%,#162039 80%)}
  .card{position:absolute;width:207px;height:130px}
  .rail{position:absolute;top:20px;width:24px;height:90px;background:var(--rail);border-radius:5px;box-shadow:inset 0 0 0 1px #2c3850}
  .rail.left{left:0}.rail.right{right:0}
  .rail::after{content:"";position:absolute;left:8px;top:14px;width:8px;height:62px;border-radius:4px;background:var(--zone);box-shadow:0 0 8px var(--zone)}
  .zone-green{--zone:var(--green)}
  .zone-orange{--zone:var(--orange)}
  .zone-red{--zone:var(--red)}
  .plate,.plate-inner{clip-path:polygon(16px 0,calc(100% - 16px) 0,100% 16px,100% calc(100% - 16px),calc(100% - 16px) 100%,16px 100%,0 calc(100% - 16px),0 16px)}
  .plate{position:absolute;left:18px;top:0;width:171px;height:130px;background:var(--cyan-line)}
  .plate-inner{position:absolute;inset:2px;background:linear-gradient(180deg,var(--plate-top),var(--plate-bottom))}
  .user-name{position:absolute;left:0;right:0;top:14px;text-align:center;color:var(--cyan);font-size:16px;font-weight:500;letter-spacing:.2px}
  .hr-pct{position:absolute;right:22px;top:43px;width:62px;height:29px;border-radius:8px;background:var(--pill);color:var(--cyan);font-size:20px;line-height:29px;text-align:center;font-weight:500}
  .bpm{position:absolute;left:26px;top:86px;width:118px;height:32px;background:linear-gradient(90deg,rgba(40,110,180,.55),rgba(40,110,180,.25));color:var(--cyan);font-size:31px;line-height:32px;padding-left:5px;font-weight:400}
  .heart{position:absolute;left:116px;top:80px;width:34px;height:32px;filter:drop-shadow(0 1px 2px rgba(0,0,0,.5))}

  /* footer */
  .ticker{position:absolute;left:0;bottom:0;width:100%;height:62px;background:var(--bar);display:flex;align-items:center}
  .rank{position:absolute;top:20px;display:flex;align-items:center;gap:6px;color:var(--white);font-size:18px}
  .rank .who{color:var(--cyan);font-size:13px}
  .rank svg{margin-left:6px}
  .divider{position:absolute;top:0;width:1px;height:62px;background:#2a3550}
  .news{position:absolute;left:607px;top:24px;color:var(--muted);font-size:12px}
  .clock{position:absolute;right:32px;top:18px;color:var(--white);font-size:20px}
</style>
</head>
<body>
<svg width="0" height="0" style="position:absolute">
  <defs>
    <radialGradient id="heartFill" cx="35%" cy="30%" r="75%">
      <stop offset="0" stop-color="#ff8a8a"/>
      <stop offset=".45" stop-color="#ee1c1c"/>
      <stop offset="1" stop-color="#a30000"/>
    </radialGradient>
    <symbol id="heart-icon" viewBox="0 0 34 32">
      <path d="M17 30 C6 21 1 15.5 1 9.5 1 4.5 5 1 9.5 1 13 1 15.5 3 17 6 18.5 3 21 1 24.5 1 29 1 33 4.5 33 9.5 33 15.5 28 21 17 30Z" fill="url(#heartFill)" stroke="#fff" stroke-width="1.8"/>
    </symbol>
  </defs>
</svg>

<main class="screen">
  <header class="topbar">
    <svg class="back-btn" width="30" height="24" viewBox="0 0 30 24" aria-label="Back"><path d="M12 3 3 12l9 9M3 12h25" fill="none" stroke="var(--cyan)" stroke-width="1.8"/></svg>
    <h1 class="system-title">System Name</h1>
    <div class="account">
      <svg width="35" height="35" viewBox="0 0 35 35" aria-hidden="true"><circle cx="17.5" cy="17.5" r="16" fill="none" stroke="var(--cyan)" stroke-width="1.6"/><circle cx="17.5" cy="13.5" r="5" fill="none" stroke="var(--cyan)" stroke-width="1.6"/><path d="M8.5 27c1.5-5 5-7 9-7s7.5 2 9 7" fill="none" stroke="var(--cyan)" stroke-width="1.6"/></svg>
      <span>Name User</span>
    </div>
    <svg class="settings-btn" width="26" height="26" viewBox="0 0 26 26" aria-label="Settings"><path d="M11 2h4l.7 3 2.2 1 2.6-1.7 2.8 2.8L21.6 9.7l1 2.2 3 .7v4l-3 .7-1 2.2 1.7 2.6-2.8 2.8-2.6-1.7-2.2 1-.7 3h-4l-.7-3-2.2-1-2.6 1.7-2.8-2.8 1.7-2.6-1-2.2-3-.7v-4l3-.7 1-2.2-1.7-2.6 2.8-2.8 2.6 1.7 2.2-1z" fill="none" stroke="var(--cyan)" stroke-width="1.5" stroke-linejoin="round"/><circle cx="13" cy="14" r="4" fill="none" stroke="var(--cyan)" stroke-width="1.5"/></svg>
  </header>

  <section class="stage" role="img" aria-label="Faint world map with grid lines behind the class roster">
    <article class="card zone-green" style="left:28px;top:45px"><span class="rail left"></span><div class="plate"><div class="plate-inner"><h2 class="user-name">#2 User name</h2><p class="hr-pct">75%</p><p class="bpm">110</p><svg class="heart"><use href="#heart-icon"/></svg></div></div><span class="rail right"></span></article>
    <article class="card zone-orange" style="left:262px;top:45px"><span class="rail left"></span><div class="plate"><div class="plate-inner"><h2 class="user-name">#15 User name</h2><p class="hr-pct">80%</p><p class="bpm">169</p><svg class="heart"><use href="#heart-icon"/></svg></div></div><span class="rail right"></span></article>
    <article class="card zone-red" style="left:495px;top:45px"><span class="rail left"></span><div class="plate"><div class="plate-inner"><h2 class="user-name">#12 User name</h2><p class="hr-pct">75%</p><p class="bpm">115</p><svg class="heart"><use href="#heart-icon"/></svg></div></div><span class="rail right"></span></article>
    <article class="card zone-green" style="left:729px;top:45px"><span class="rail left"></span><div class="plate"><div class="plate-inner"><h2 class="user-name">#7 User name</h2><p class="hr-pct">75%</p><p class="bpm">112</p><svg class="heart"><use href="#heart-icon"/></svg></div></div><span class="rail right"></span></article>
    <article class="card zone-green" style="left:963px;top:45px"><span class="rail left"></span><div class="plate"><div class="plate-inner"><h2 class="user-name">#9 User name</h2><p class="hr-pct">75%</p><p class="bpm">158</p><svg class="heart"><use href="#heart-icon"/></svg></div></div><span class="rail right"></span></article>

    <article class="card zone-green" style="left:28px;top:208px"><span class="rail left"></span><div class="plate"><div class="plate-inner"><h2 class="user-name">#4 User name</h2><p class="hr-pct">88%</p><p class="bpm">114</p><svg class="heart"><use href="#heart-icon"/></svg></div></div><span class="rail right"></span></article>
    <article class="card zone-orange" style="left:262px;top:208px"><span class="rail left"></span><div class="plate"><div class="plate-inner"><h2 class="user-name">#8 User name</h2><p class="hr-pct">95%</p><p class="bpm">178</p><svg class="heart"><use href="#heart-icon"/></svg></div></div><span class="rail right"></span></article>
    <article class="card zone-red" style="left:495px;top:208px"><span class="rail left"></span><div class="plate"><div class="plate-inner"><h2 class="user-name">#1 User name</h2><p class="hr-pct">97%</p><p class="bpm">111</p><svg class="heart"><use href="#heart-icon"/></svg></div></div><span class="rail right"></span></article>
    <article class="card zone-green" style="left:729px;top:208px"><span class="rail left"></span><div class="plate"><div class="plate-inner"><h2 class="user-name">#19 User name</h2><p class="hr-pct">80%</p><p class="bpm">75</p><svg class="heart"><use href="#heart-icon"/></svg></div></div><span class="rail right"></span></article>
    <article class="card zone-green" style="left:963px;top:208px"><span class="rail left"></span><div class="plate"><div class="plate-inner"><h2 class="user-name">#21 User name</h2><p class="hr-pct">87%</p><p class="bpm">169</p><svg class="heart"><use href="#heart-icon"/></svg></div></div><span class="rail right"></span></article>

    <article class="card zone-green" style="left:28px;top:371px"><span class="rail left"></span><div class="plate"><div class="plate-inner"><h2 class="user-name">#12 User name</h2><p class="hr-pct">75%</p><p class="bpm">110</p><svg class="heart"><use href="#heart-icon"/></svg></div></div><span class="rail right"></span></article>
    <article class="card zone-orange" style="left:262px;top:371px"><span class="rail left"></span><div class="plate"><div class="plate-inner"><h2 class="user-name">#17 User name</h2><p class="hr-pct">72%</p><p class="bpm">144</p><svg class="heart"><use href="#heart-icon"/></svg></div></div><span class="rail right"></span></article>
    <article class="card zone-red" style="left:495px;top:371px"><span class="rail left"></span><div class="plate"><div class="plate-inner"><h2 class="user-name">#16 User name</h2><p class="hr-pct">99%</p><p class="bpm">69</p><svg class="heart"><use href="#heart-icon"/></svg></div></div><span class="rail right"></span></article>
    <article class="card zone-green" style="left:729px;top:371px"><span class="rail left"></span><div class="plate"><div class="plate-inner"><h2 class="user-name">#25 User name</h2><p class="hr-pct">94%</p><p class="bpm">120</p><svg class="heart"><use href="#heart-icon"/></svg></div></div><span class="rail right"></span></article>
    <article class="card zone-green" style="left:963px;top:371px"><span class="rail left"></span><div class="plate"><div class="plate-inner"><h2 class="user-name">#33 User name</h2><p class="hr-pct">82%</p><p class="bpm">145</p><svg class="heart"><use href="#heart-icon"/></svg></div></div><span class="rail right"></span></article>
  </section>

  <footer class="ticker">
    <div class="rank" style="left:23px"><span>12.</span><span class="who">#12 User name</span><svg width="14" height="11" viewBox="0 0 14 11"><path d="M7 0 14 11H0z" fill="var(--green)"/></svg></div>
    <div class="rank" style="left:208px"><span>17.</span><span class="who">#17 User name</span><svg width="14" height="11" viewBox="0 0 14 11"><path d="M7 0 14 11H0z" fill="var(--green)"/></svg></div>
    <div class="rank" style="left:399px"><span>16.</span><span class="who">#16 User name</span><svg width="14" height="11" viewBox="0 0 14 11"><path d="M0 0h14L7 11z" fill="var(--red)"/></svg></div>
    <span class="divider" style="left:596px"></span>
    <p class="news">Lorem ipsum dolor sit amet, consectetuer adipiscing elit, sed diam nonummy</p>
    <span class="divider" style="left:1084px"></span>
    <time class="clock">08:45</time>
  </footer>
</main>
</body>
</html>
```